Menu Board 1000mmx500mm re-design

I would like to re-design exiting menu board 1000mmx500mm. Current board letters are bit to small to read. I would like to have pictures (attached) of the food offered on it and at the same time to create balance between pictures and size of the text to be easily readable. Fonts and colours are up to designer choice but prefer warm and bright colours rather anything dark.

Target Market(s)

Food industry

Industry/Entity Type

Food

Font styles to use
Other font styles liked:
• I leave font choice to designer

Colors
FFC000
F8CF3A
FAE287
FDF2CF
FEFAEE
F0912C
F2A743
F7CA91
FBE8D2
FDF5EE
EE7325
F08F49
F5BC92
FAE3D3
FDF4ED

Requirements
Must have
• Pictures + Text
Nice to have
• Balance between images and text.
Should not have
• Can't think of any

```html
<!DOCTYPE html>
<html lang="en">
<head>
<meta charset="utf-8">
<title>Menu Board</title>
<link href="https://fonts.googleapis.com/css2?family=Luckiest+Guy&family=Montserrat:wght@400;500;700;800&display=swap" rel="stylesheet">
<style>
  :root {
    --page: #e3e0df;
    --board-top: #2f1e19;
    --board-mid: #1c0b08;
    --board-bottom: #120404;
    --orange: #ee7325;
    --orange-soft: #f08f49;
    --bar: #3a2620;
    --cream: #fdf2cf;
    --white: #ffffff;
    --ink: #1a0a06;
    --yellow: #ffc000;
    --brick-a: #5a1c14;
    --brick-b: #2a0c08;
  }
  * { box-sizing: border-box; margin: 0; padding: 0; }
  html, body { width: 725px; height: 1200px; overflow: hidden; background: var(--page); }
  body { position: relative; font-family: "Montserrat", sans-serif; }

  .board {
    position: absolute; left: 62px; top: 0; width: 600px; height: 1200px;
    background: linear-gradient(180deg, var(--board-top) 0%, var(--board-mid) 45%, var(--board-bottom) 80%);
    overflow: hidden;
  }

  .hero-frame { position: absolute; left: 0; top: 0; width: 600px; height: 390px; }
  .hero-photo {
    position: absolute; left: 61px; top: 78px; width: 483px; height: 160px;
    border-radius: 50% 50% 46% 46% / 30% 30% 70% 70%;
    background: radial-gradient(ellipse at 50% 40%, #d9a35f 0%, #a7682f 45%, #5e3a1c 80%, rgba(46,30,25,0) 100%);
  }
  .menu-title {
    position: absolute; left: 0; right: 0; top: 246px; text-align: center;
    font-family: "Luckiest Guy", sans-serif; font-size: 118px; line-height: 1;
    font-weight: 400;
    color: var(--orange); letter-spacing: 1px;
    -webkit-text-stroke: 3px var(--ink);
    text-shadow: 0 4px 0 var(--ink);
  }

  .menu-list { position: absolute; left: 0; top: 0; width: 600px; }
  .item { position: absolute; left: 0; width: 600px; height: 80px; }
  .item-photo {
    position: absolute; left: 60px; top: 0; width: 96px; height: 70px;
    border-radius: 3px;
    background: linear-gradient(135deg, var(--orange) 0%, #c98a45 50%, #7a4a22 100%);
  }
  .item-bar {
    position: absolute; left: 179px; top: 0; width: 260px; height: 32px;
    background: linear-gradient(90deg, var(--bar), #2a1814);
    color: var(--white); font-weight: 700; font-size: 20px; line-height: 32px;
    padding-left: 17px; white-space: nowrap;
  }
  .item-price {
    position: absolute; left: 439px; top: 0; width: 75px; height: 32px;
    background: var(--orange); color: var(--white);
    font-weight: 800; font-size: 21px; line-height: 32px; text-align: center;
  }
  .item-desc {
    position: absolute; left: 179px; top: 42px; width: 380px;
    color: var(--white); font-size: 11.6px; line-height: 16.5px; font-weight: 400;
    white-space: nowrap;
  }

  .drinks { position: absolute; left: 0; top: 951px; width: 600px; height: 50px; }
  .drink-label {
    position: absolute; top: 0; height: 34px; background: var(--white);
    color: var(--ink); font-weight: 800; font-size: 20px; line-height: 34px; padding-left: 13px;
    white-space: nowrap;
  }
  .drink-price {
    position: absolute; top: -7px; width: 46px; height: 46px; border-radius: 50%;
    background: var(--ink); border: 2px solid var(--orange);
    box-shadow: 0 0 0 3px var(--ink), 0 0 0 4px var(--white);
    color: var(--orange); font-weight: 800; font-size: 13px; line-height: 42px; text-align: center;
  }

  .sauces-band {
    position: absolute; left: 0; top: 1025px; width: 600px; height: 175px;
    background:
      repeating-linear-gradient(0deg, rgba(0,0,0,.18) 0 1px, transparent 1px 10px),
      radial-gradient(ellipse at 55% 40%, var(--brick-a) 0%, var(--brick-b) 80%);
  }
  .sauces-frame {
    position: absolute; left: 43px; top: 17px; width: 513px; height: 124px;
    border: 1.5px solid var(--white);
  }
  .sauces-divider { position: absolute; left: 146px; top: 8px; width: 1px; height: 106px; background: rgba(255,255,255,.2); }
  .sauces-title {
    position: absolute; left: -9px; top: 44px; padding: 0 4px;
    color: var(--white); font-weight: 700; font-size: 32px; line-height: 36px;
    background: linear-gradient(90deg, #3a1009, #4a150e);
  }
  .sauce {
    position: absolute; display: flex; align-items: center; gap: 6px;
    color: var(--orange); font-weight: 700; font-size: 17px; line-height: 20px; white-space: nowrap;
  }
  .sauce svg { width: 15px; height: 18px; flex: none; }
</style>
</head>
<body>
<main class="board">
  <svg class="hero-frame" viewBox="0 0 600 390" aria-hidden="true">
    <path d="M36 36 L565 68 L565 362 Q565 380 547 380 L54 380 Q36 380 36 362 Z" fill="none" stroke="#ee7325" stroke-width="2.5"/>
  </svg>
  <div class="hero-photo" role="img" aria-label="Chicken ciabatta with rocket and roasted potatoes on a wooden board, with a halved wrap beside it"></div>
  <h1 class="menu-title">MENU</h1>

  <section class="menu-list">
    <article class="item" style="top:419px">
      <div class="item-photo" role="img" aria-label="Chicken ciabatta with rocket"></div>
      <h2 class="item-bar">CIABATTA</h2>
      <div class="item-price">£6</div>
      <p class="item-desc">Roti Chicken, Rucola, Caramelized<br>Onions, Tomato, Fresh Onion</p>
    </article>
    <article class="item" style="top:505px">
      <div class="item-photo" role="img" aria-label="Halved chicken wrap with salad"></div>
      <h2 class="item-bar">WRAP</h2>
      <div class="item-price">£7</div>
      <p class="item-desc">Roti Chicken, Crunchy Slaw, Tomato,<br>Fresh Onion &amp; Sauce of your choice</p>
    </article>
    <article class="item" style="top:597px">
      <div class="item-photo" role="img" aria-label="Halved beetroot wrap with chicken and slaw"></div>
      <h2 class="item-bar">BEETROOT WRAP</h2>
      <div class="item-price">£8</div>
      <p class="item-desc">Roti Chicken, Crunchy Slaw, Tomato, Fresh Onion &amp;<br>Sauce of your choice</p>
    </article>
    <article class="item" style="top:682px">
      <div class="item-photo" role="img" aria-label="Grilled chicken wrap on a wooden board"></div>
      <h2 class="item-bar">CHICKEN BOX 1/4</h2>
      <div class="item-price">£9</div>
      <p class="item-desc">Roti Chicken, Veggie Rice &amp; Salad</p>
    </article>
    <article class="item" style="top:766px">
      <div class="item-photo" role="img" aria-label="Roast chicken leg with vegetable rice in a wooden bowl"></div>
      <h2 class="item-bar">CHICKEN BOX 1/2</h2>
      <div class="item-price">£14</div>
      <p class="item-desc">Roti Chicken, Veggie Rice &amp; Salad</p>
    </article>
    <article class="item" style="top:857px">
      <div class="item-photo" role="img" aria-label="Roasted potatoes with a sprig of rosemary"></div>
      <h2 class="item-bar">ROASTED POTATOES</h2>
      <div class="item-price">£25</div>
      <p class="item-desc">Thyme &amp; Garlic</p>
    </article>
  </section>

  <section class="drinks">
    <div class="drink-label" style="left:94px;width:115px">WATER</div>
    <div class="drink-price" style="left:194px">£1</div>
    <div class="drink-label" style="left:287px;width:185px">CAN &amp; JUICES</div>
    <div class="drink-price" style="left:462px">£1.8</div>
  </section>

  <section class="sauces-band">
    <div class="sauces-frame">
      <h2 class="sauces-title">SAUCES</h2>
      <div class="sauces-divider"></div>
      <span class="sauce" style="left:172px;top:26px"><svg viewBox="0 0 15 18"><path d="M7.5 17 C3 11 1 8.5 1 6.5 A6.5 6.5 0 0 1 14 6.5 C14 8.5 12 11 7.5 17Z" fill="#fff"/><circle cx="7.5" cy="6.5" r="3.6" fill="#ee7325"/></svg>SIGNATURE</span>
      <span class="sauce" style="left:317px;top:26px"><svg viewBox="0 0 15 18"><path d="M7.5 17 C3 11 1 8.5 1 6.5 A6.5 6.5 0 0 1 14 6.5 C14 8.5 12 11 7.5 17Z" fill="#fff"/><circle cx="7.5" cy="6.5" r="3.6" fill="#ee7325"/></svg>BBQ</span>
      <span class="sauce" style="left:395px;top:26px"><svg viewBox="0 0 15 18"><path d="M7.5 17 C3 11 1 8.5 1 6.5 A6.5 6.5 0 0 1 14 6.5 C14 8.5 12 11 7.5 17Z" fill="#fff"/><circle cx="7.5" cy="6.5" r="3.6" fill="#ee7325"/></svg>PIRI PIRI</span>
      <span class="sauce" style="left:172px;top:61px"><svg viewBox="0 0 15 18"><path d="M7.5 17 C3 11 1 8.5 1 6.5 A6.5 6.5 0 0 1 14 6.5 C14 8.5 12 11 7.5 17Z" fill="#fff"/><circle cx="7.5" cy="6.5" r="3.6" fill="#ee7325"/></svg>SWEET CHILLI</span>
      <span class="sauce" style="left:340px;top:61px"><svg viewBox="0 0 15 18"><path d="M7.5 17 C3 11 1 8.5 1 6.5 A6.5 6.5 0 0 1 14 6.5 C14 8.5 12 11 7.5 17Z" fill="#fff"/><circle cx="7.5" cy="6.5" r="3.6" fill="#ee7325"/></svg>GARLIC MAYO</span>
    </div>
  </section>
</main>
</body>
</html>
```